Icon-Design für Makeup Artist Webseite
Super creative designs. Exactly what we were looking for!Highly recommended.
Zielgruppe
Sabine Ter Horst Makeup Artist. Zielgruppe 18-34. 'Normale' Personen die lernen wollen wie man Makeup richtig aufträgt.
Aufgabenstellung
Das Projekt besteht darin 5 Icons zu designen. Die Webseite ist noch in der Entwicklung ein Screenshot wie es auf dem Handy aussehen soll finden Sie im Anhang.
Es werden 5 creative Icons benötigt die die Kategorien wiederspiegeln.(Also keine "Langweiligen Icone", diese können ruhig ausgefallen sein, sollten jedoch zum style der Seite passen )
Kategorie 1 = Eye Makeup(Lidschatten) Tutorials. Hier sind Texte + Videos enthalten wie man das Augenmakeup richtig aufträgt + Ausgefallene Looks
Kategorie 2 = Skin Care. Texte+Bilder über Haut+Produkte zur richtigen Pflege seiner Haut.
Kategorie 3 = E-Book. Hier steht ein E-Book-Shop zur verfügung indem man sich E-Book kaufen kann.
Kategorie 4 = About. Hier sind alle Informationen über Sabine enthalten.
Download Button = Dieser sollte auf einem leicht grauen-weißen hintergrund ordentlich zum vorschein kommen.
Der Blaue Farb-Code der Webseite ist : 3b5998

```html
<!DOCTYPE html>
<html lang="de">
<head>
<meta charset="utf-8">
<title>Kategorie-Icons</title>
<link rel="stylesheet" href="https://fonts.googleapis.com/css2?family=Gochi+Hand&family=Open+Sans:wght@400&display=swap">
<style>
  :root {
    --brand-blue: #3b5998;
    --ink: #000000;
    --paper: #ffffff;
    --paper-soft: #dfe5f1;
  }
  * { margin: 0; padding: 0; box-sizing: border-box; }
  html, body {
    width: 1200px;
    height: 675px;
    overflow: hidden;
    background: var(--paper);
  }
  .icon-board {
    position: relative;
    width: 1200px;
    height: 675px;
    background: var(--paper);
  }
  .category {
    position: absolute;
    width: 200px;
    height: 200px;
  }
  .category svg { display: block; width: 200px; height: 200px; }
  .category--makeup   { left: 503px; top: 51px; }
  .category--about    { left: 276px; top: 311px; }
  .category--ebook    { left: 503px; top: 311px; }
  .category--skincare { left: 751px; top: 311px; }

  .category-label {
    position: absolute;
    transform: translateX(-50%);
    font-family: "Gochi Hand", cursive;
    font-size: 44px;
    line-height: 1;
    color: var(--ink);
    white-space: nowrap;
  }
  .label--makeup   { left: 606px; top: 250px; word-spacing: 14px; }
  .label--about    { left: 370px; top: 507px; }
  .label--ebook    { left: 605px; top: 514px; }
  .label--skincare { left: 851px; top: 517px; }

  .download-button {
    position: absolute;
    left: 470px;
    top: 587px;
    width: 259px;
    height: 63px;
    border-radius: 26px;
    background: var(--brand-blue);
    color: var(--paper);
    font-family: "Open Sans", sans-serif;
    font-size: 39px;
    line-height: 63px;
    display: flex;
    align-items: center;
    padding-left: 12px;
    gap: 8px;
    text-decoration: none;
  }
  .download-button svg { width: 28px; height: 24px; flex: none; }
</style>
</head>
<body>
<main class="icon-board">

  <div class="category category--makeup">
    <svg viewBox="0 0 200 200" aria-hidden="true">
      <defs>
        <linearGradient id="symbol-fill" x1="0" y1="0" x2="0" y2="1">
          <stop offset="0" stop-color="var(--paper)"/>
          <stop offset="1" stop-color="var(--paper-soft)"/>
        </linearGradient>
      </defs>
      <circle cx="100" cy="100" r="100" fill="var(--brand-blue)"/>
      <rect class="symbol-area" x="51" y="32" width="99" height="136" rx="40" fill="url(#symbol-fill)" role="img" aria-label="Illustration einer geöffneten Puderdose mit Spiegel"/>
    </svg>
  </div>
  <span class="category-label label--makeup">Make Up</span>

  <div class="category category--about">
    <svg viewBox="0 0 200 200" aria-hidden="true">
      <circle cx="100" cy="100" r="100" fill="var(--brand-blue)"/>
      <path d="M100 34 C 165 34 180 90 158 128 C 146 150 124 168 100 182 L 100 158 C 60 160 34 130 34 96 C 34 60 62 34 100 34 Z" fill="var(--paper)"/>
      <rect x="93" y="57" width="16" height="14" rx="7" fill="var(--brand-blue)"/>
      <rect x="93" y="85" width="15" height="43" fill="var(--brand-blue)"/>
    </svg>
  </div>
  <span class="category-label label--about">About</span>

  <div class="category category--ebook">
    <svg viewBox="0 0 200 200" aria-hidden="true">
      <circle cx="100" cy="100" r="100" fill="var(--brand-blue)"/>
      <rect x="48" y="30" width="104" height="139" rx="9" fill="var(--paper)"/>
      <rect x="60" y="42" width="80" height="105" rx="3" fill="var(--brand-blue)"/>
      <circle cx="100" cy="157" r="4" fill="var(--brand-blue)"/>
    </svg>
  </div>
  <span class="category-label label--ebook">E-Book</span>

  <div class="category category--skincare">
    <svg viewBox="0 0 200 200" aria-hidden="true">
      <defs>
        <linearGradient id="symbol-fill-skin" x1="0" y1="0" x2="0" y2="1">
          <stop offset="0" stop-color="var(--paper)"/>
          <stop offset="1" stop-color="var(--paper-soft)"/>
        </linearGradient>
      </defs>
      <circle cx="100" cy="100" r="100" fill="var(--brand-blue)"/>
      <rect class="symbol-area" x="43" y="28" width="112" height="148" rx="40" fill="url(#symbol-fill-skin)" role="img" aria-label="Illustration eines Frauenprofils als Silhouette"/>
    </svg>
  </div>
  <span class="category-label label--skincare">Skincare</span>

  <a class="download-button" href="#download">
    <svg viewBox="0 0 28 24" aria-hidden="true"><polygon points="0,0 28,0 14,24" fill="var(--paper)"/></svg>
    <span>Download</span>
  </a>

</main>
</body>
</html>
```